Sticker proposal and a brand name for matured cheese slices

We need a full face sticker design and a brand name for a packaging of cheese slices. The cheese is mature holland gouda (aged for 2-3 months) and lactose free which we want to be addressed. Dimensions of the sticker should be 140x115mm. We want to make up a name for the packages like brovintel did, but not based on the origin of the cheese. The market we are going to sell at first is the greek one. Our Company is VELMIRA SA and website, velmira-sa.com. The sticker style should be modern, referring to nature, tradition or technology and bright coloured.

Reason: we need more designs to choose from

Target Market(s)

supermarkets

Industry/Entity Type

Food Store

Requirements
Must have
• lactose free, mature, slices
Nice to have
• blue, green colours. a transparent hole so that the cheese slice can be seen. toast/sandwich figure as it is mostly used for sandwich
Should not have
• dark colours

```html
<!DOCTYPE html>
<html lang="en">
<head>
<meta charset="utf-8">
<title>VELMIRA – Lactose Free Aged Holland Gouda</title>
<link rel="stylesheet" href="https://fonts.googleapis.com/css2?family=Federo&family=Montserrat:wght@500&family=Sriracha&display=swap">
<style>
  :root {
    --page: #ffffff;
    --cream: #fcf1dc;
    --frame-blue: #8fc0ec;
    --deep-blue: #2b63aa;
    --sky-blue: #7eb6ea;
    --gold: #c4962a;
    --photo-light: #f3e6b4;
    --photo-mid: #ead9a4;
  }
  html, body {
    margin: 0;
    padding: 0;
    width: 729px;
    height: 1200px;
    overflow: hidden;
    background: var(--page);
  }
  .sticker {
    position: relative;
    width: 729px;
    height: 1200px;
  }
  .label-panel {
    position: absolute;
    left: 9px;
    top: 90px;
    width: 713px;
    height: 1021px;
    background: var(--cream);
  }
  .frame {
    position: absolute;
    left: 0;
    top: 0;
  }
  .brand-name {
    position: absolute;
    left: 0;
    width: 729px;
    top: 56px;
    margin: 0;
    text-align: center;
    font-family: "Federo", sans-serif;
    font-weight: 400;
    font-size: 56px;
    line-height: 1;
    color: var(--deep-blue);
    letter-spacing: 1px;
  }
  .claim {
    position: absolute;
    margin: 0;
    font-family: "Sriracha", cursive;
    color: var(--deep-blue);
    line-height: 1;
    white-space: nowrap;
    transform: rotate(-4deg);
    transform-origin: left bottom;
  }
  .claim-lactose { left: 184px; top: 218px; font-size: 92px; }
  .claim-free { left: 398px; top: 296px; font-size: 84px; }
  .serving-photo {
    position: absolute;
    left: 120px;
    top: 465px;
    width: 490px;
    height: 253px;
    border-radius: 24px;
    background: linear-gradient(180deg, var(--photo-light) 0%, var(--photo-mid) 100%);
  }
  .product-type {
    position: absolute;
    left: 0;
    width: 729px;
    top: 783px;
    margin: 0;
    text-align: center;
    font-family: "Montserrat", sans-serif;
    font-weight: 500;
    font-size: 30px;
    line-height: 1;
    letter-spacing: 8px;
    text-indent: 8px;
    color: var(--sky-blue);
  }
  .product-age {
    position: absolute;
    left: 0;
    width: 729px;
    top: 838px;
    margin: 0;
    text-align: center;
    font-family: "Federo", sans-serif;
    font-weight: 400;
    font-size: 88px;
    line-height: 1;
    color: var(--deep-blue);
  }
  .product-name {
    position: absolute;
    left: 0;
    width: 729px;
    top: 940px;
    margin: 0;
    text-align: center;
    font-family: "Federo", sans-serif;
    font-weight: 400;
    font-size: 58px;
    line-height: 1;
    letter-spacing: 1px;
    color: var(--deep-blue);
  }
  .net-weight {
    position: absolute;
    right: 81px;
    top: 1037px;
    margin: 0;
    font-family: "Montserrat", sans-serif;
    font-weight: 500;
    font-size: 22px;
    line-height: 1;
    color: var(--gold);
  }
</style>
</head>
<body>
<div class="sticker">
  <div class="label-panel"></div>

  <svg class="frame" width="729" height="1200" viewBox="0 0 729 1200" aria-hidden="true">
    <g fill="none" stroke="var(--frame-blue)" stroke-width="3">
      <polyline points="190,112 25,112 25,1097 335,1097"/>
      <polyline points="548,112 707,112 707,1097 409,1097"/>
      <polyline points="190,123 36,123 36,1086 335,1086"/>
      <polyline points="548,123 696,123 696,1086 409,1086"/>
    </g>
    <polygon class="ribbon" points="334,1052 371,1076 408,1052 408,1200 334,1200" fill="var(--sky-blue)"/>
  </svg>

  <h1 class="brand-name">VELMIRA</h1>

  <p class="claim claim-lactose">Lactose</p>
  <p class="claim claim-free">free</p>

  <div class="serving-photo" role="img" aria-label="Photo area: slices of aged gouda on wholegrain bread"></div>

  <p class="product-type">SLICED</p>
  <h2 class="product-age">AGED</h2>
  <h2 class="product-name">HOLLAND GOUDA</h2>
  <p class="net-weight">160g Net</p>
</div>
</body>
</html>
```